BLUE HAVEN (Business Card for Training Company)

Blue Haven is a training and consultancy company with a focus on executive protection and medical. I would like the card to be nice and sharp, not overdone and in black and red. I would also like it to highlight that it is "A Dravin Company"

I would like it to be simple and highlight a few things.

1. Name
2. Title
3. Phone Number
4. Email

I would also like www.dravinholdings.example/blue-haven to be on the card somewhere.

Target Market(s)

Security Companies

Industry/Entity Type

Security

Contact Information for Business Card

Blue Haven is a training and consultancy company with a focus on executive protection and medical. I would like the card to be nice and sharp, not overdone and in black and red. I would also like it to highlight that it is "A Dravin Company" I would like it to be simple and highlight a few things. 1. Name 2. Title 3. Phone Number 4. Email I would also like www.dravinholdings.example/blue-haven to be on the card somewhere.

Requirements
Must have
• A Dravin Company listed on the card and the website
Nice to have
• Highlight Medical Training, Consultancy & Executive Protection Courses

```html
<!DOCTYPE html>
<html lang="en">
<head>
<meta charset="utf-8">
<title>Blue Haven — Business Card</title>
<link href="https://fonts.googleapis.com/css2?family=Roboto+Condensed:wght@400;700&family=Roboto:wght@500&family=Michroma&display=swap" rel="stylesheet">
<style>
  :root {
    --bg: #e4e4e4;
    --card: #f6f6f6;
    --red: #7a0a0a;
    --ink: #111111;
    --grey: #555555;
    --rule: #333333;
  }
  html, body {
    margin: 0;
    width: 1200px;
    height: 1200px;
    overflow: hidden;
    background: var(--bg);
  }
  .canvas { position: relative; width: 1200px; height: 1200px; }
  .card {
    position: absolute;
    left: 262px;
    width: 686px;
    height: 392px;
    background: var(--card);
    box-shadow: 0 14px 24px rgba(0,0,0,0.18);
    overflow: hidden;
    font-family: "Roboto Condensed", sans-serif;
  }
  .card--front { top: 165px; }
  .card--back { top: 653px; }

  .wordmark {
    position: absolute;
    font-family: "Roboto Condensed", sans-serif;
    font-weight: 700;
    color: var(--ink);
    line-height: 0.92;
    text-transform: uppercase;
    margin: 0;
  }
  .parent-line {
    position: absolute;
    font-family: "Roboto", sans-serif;
    font-weight: 500;
    color: var(--grey);
    text-transform: uppercase;
    margin: 0;
    white-space: nowrap;
  }

  /* front */
  .card--front .wordmark { right: 50px; top: 54px; font-size: 50px; letter-spacing: 1px; }
  .card--front .parent-line { right: 48px; top: 155px; font-size: 15px; letter-spacing: 3.4px; }
  .holder-name {
    position: absolute; left: 41px; top: 232px; margin: 0;
    font-family: "Michroma", sans-serif; font-size: 21px; color: var(--red);
    letter-spacing: 0.5px;
  }
  .holder-title {
    position: absolute; left: 41px; top: 260px; margin: 0;
    font-size: 18px; color: var(--ink);
  }
  .divider {
    position: absolute; left: 41px; top: 291px; width: 594px; height: 1px;
    background: var(--rule);
  }
  .contact { position: absolute; left: 41px; top: 304px; margin: 0; padding: 0; list-style: none; }
  .contact li {
    display: flex; align-items: center; gap: 8px;
    font-size: 18px; color: #333; height: 22px;
  }
  .contact svg { width: 13px; height: 13px; fill: var(--red); }
  .website {
    position: absolute; right: 50px; top: 324px; margin: 0;
    font-size: 17px; color: var(--red);
  }
  .accent-band {
    position: absolute; left: 0; bottom: 0; width: 100%; height: 12px;
    background: var(--red);
  }

  /* back */
  .card--back .wordmark {
    left: 0; right: 0; top: 112px; text-align: center; font-size: 66px; letter-spacing: 2px;
  }
  .card--back .parent-line {
    left: 0; right: 0; top: 254px; text-align: center; font-size: 22px; letter-spacing: 5px;
  }
  .tagline {
    position: absolute; left: 0; right: 0; top: 336px; margin: 0;
    text-align: center; font-size: 18px; color: var(--ink);
  }
  .tagline .tagline__lead { color: var(--red); }
</style>
</head>
<body>
<main class="canvas">

  <section class="card card--front" aria-label="Business card front">
    <h1 class="wordmark">Blue<br>Haven</h1>
    <p class="parent-line">A Dravin Company</p>

    <h2 class="holder-name">DANIEL HART</h2>
    <p class="holder-title">President</p>
    <div class="divider"></div>

    <ul class="contact">
      <li>
        <svg viewBox="0 0 24 24" aria-hidden="true"><path d="M6.6 10.8a15.1 15.1 0 0 0 6.6 6.6l2.2-2.2a1 1 0 0 1 1-.25 11.4 11.4 0 0 0 3.6.6 1 1 0 0 1 1 1V20a1 1 0 0 1-1 1A17 17 0 0 1 3 4a1 1 0 0 1 1-1h3.5a1 1 0 0 1 1 1c0 1.25.2 2.45.6 3.6a1 1 0 0 1-.25 1z"/></svg>
        555-014-2738
      </li>
      <li>
        <svg viewBox="0 0 24 24" aria-hidden="true"><path d="M2 5h20v14H2z M4 7v.5l8 5 8-5V7l-8 5z" fill-rule="evenodd"/></svg>
        info@dravinholdings.example
      </li>
    </ul>
    <p class="website">www.dravinholdings.example</p>
    <div class="accent-band"></div>
  </section>

  <section class="card card--back" aria-label="Business card back">
    <h1 class="wordmark">Blue<br>Haven</h1>
    <p class="parent-line">A Dravin Company</p>
    <p class="tagline"><span class="tagline__lead">Medical Training, Consultancy &amp;</span> Executive Protection Courses</p>
  </section>

</main>
</body>
</html>
```